Mabel's Fitness Business Cards

I would like my business cards to look expensive and sophisticated using my logo and the information below.

FRONT
Mabel’s Fitness logo

Tag line Become your happiest, healthiest and strongest self

Mabel Quint Harlow
Personal Trainer

e. mabel@mabelsfitstudio.example

t. 0781530462

w. www.mabelsfitstudio.example

```html
<!DOCTYPE html>
<html lang="en">
<head>
<meta charset="utf-8">
<title>Mabel's Fitness – Business Cards</title>
<link href="https://fonts.googleapis.com/css2?family=Jost:wght@400;500&display=swap" rel="stylesheet">
<style>
  :root {
    --teal: #6cb6c1;
    --teal-deep: #4fa3b1;
    --grey: #7d7e80;
    --grey-text: #6e6f72;
    --faint: #efeded;
    --paper: #ffffff;
    --backdrop: #e4e4e4;
  }
  * { margin: 0; padding: 0; box-sizing: border-box; }
  html, body {
    width: 837px; height: 1200px; overflow: hidden;
    background: var(--backdrop);
    font-family: "Jost", "Futura", sans-serif;
  }
  .sheet {
    width: 837px; height: 1200px;
    display: flex; flex-direction: column; align-items: center; justify-content: center;
    gap: 90px;
  }
  .card {
    position: relative; width: 700px; height: 400px; overflow: hidden;
    box-shadow: 0 6px 14px rgba(0,0,0,0.22);
  }
  .card-front { background: var(--paper); }
  .card-back { background: var(--teal); color: var(--paper); text-align: center; }
  .card svg.art { position: absolute; inset: 0; }

  .brand { position: absolute; text-align: center; font-weight: 400; }
  .brand-mark { display: block; margin: 0 auto 16px; border-radius: 50%; }
  .brand-name { display: block; text-transform: uppercase; line-height: 1.15; }

  .card-front .brand { left: 440px; top: 62px; width: 200px; color: var(--teal); }
  .card-front .brand-mark { width: 96px; height: 96px; border: 6px solid var(--teal); }
  .card-front .brand-name.primary { font-size: 25px; letter-spacing: 7px; }
  .card-front .brand-name.secondary { font-size: 14px; letter-spacing: 15px; }

  .holder { position: absolute; left: 56px; top: 204px; color: var(--grey-text); }
  .holder-name { font-size: 20px; font-weight: 500; color: var(--teal-deep); }
  .holder-role { font-size: 14px; margin-top: 1px; }
  .divider { display: flex; gap: 8px; margin: 14px 0 18px; }
  .divider span { width: 14px; height: 2px; background: var(--teal); }
  .contact { list-style: none; font-size: 14px; }
  .contact li { display: flex; align-items: center; gap: 10px; height: 21px; }
  .contact svg { width: 11px; height: 11px; fill: none; stroke: var(--teal); stroke-width: 1.6; }

  .card-back .brand { left: 0; right: 0; top: 68px; color: var(--paper); }
  .card-back .brand-mark { width: 126px; height: 126px; border: 7px solid var(--paper); margin-bottom: 22px; }
  .card-back .brand-name.primary { font-size: 31px; letter-spacing: 10px; }
  .card-back .brand-name.secondary { font-size: 17px; letter-spacing: 19px; }
  .tagline { position: absolute; left: 0; right: 0; top: 330px; font-size: 15px; }
</style>
</head>
<body>
<main class="sheet">
  <section class="card card-front" aria-label="Business card front">
    <svg class="art" viewBox="0 0 700 400" aria-hidden="true">
      <circle cx="120" cy="110" r="200" fill="none" stroke="var(--faint)" stroke-width="12"/>
      <path d="M0,400 L0,396 C230,392 500,350 700,232 L700,400 Z" fill="var(--grey)"/>
      <path d="M0,388 C240,384 470,350 640,270" fill="none" stroke="var(--teal)" stroke-width="4"/>
    </svg>

    <div class="brand">
      <span class="brand-mark"></span>
      <span class="brand-name primary">Mabel’s</span>
      <span class="brand-name secondary">Fitness</span>
    </div>

    <div class="holder">
      <p class="holder-name">Mabel Quint Harlow</p>
      <p class="holder-role">Personal Trainer</p>
      <div class="divider"><span></span><span></span><span></span></div>
      <ul class="contact">
        <li><svg viewBox="0 0 12 12"><path d="M3 1 L5 3.5 L4 5 Q5.5 7.5 7 8 L8.5 7 L11 9 L9.5 11 Q4 10.5 1 3 Z"/></svg>078 153 0462</li>
        <li><svg viewBox="0 0 12 12"><rect x="1" y="2.5" width="10" height="7"/><path d="M1 2.5 L6 6.5 L11 2.5"/></svg>mabel@mabelsfitstudio.example</li>
        <li><svg viewBox="0 0 12 12"><circle cx="6" cy="6" r="5"/><path d="M1 6 H11 M6 1 Q3 6 6 11 Q9 6 6 1"/></svg>www.mabelsfitstudio.example</li>
      </ul>
    </div>
  </section>

  <section class="card card-back" aria-label="Business card back">
    <div class="brand">
      <span class="brand-mark"></span>
      <span class="brand-name primary">Mabel’s</span>
      <span class="brand-name secondary">Fitness</span>
    </div>
    <p class="tagline">Become your happiest, healthiest and strongest self</p>
  </section>
</main>
</body>
</html>
```